Smart Home App Needs 4 Mockup Screens. Extra Work Guaranteed for Winner

BACKGROUND
Our company, Marlow, is launching an exciting new app early next year. And we need some examples of what our app will look like to show to some of the biggest retailers in the world. We hope that this project will lead to regular work as we have a lot of new products planned for the app.

Our app will support baby, home and pet monitors (cameras) as well as the world's first smart pet flap.

The monitors allow you to do much more than just watch live video. By monitoring and providing information on sound, movement and temperature the app provides the user with instant peace of mind wherever they are. If anything has changed the user can be alerted via notifications. If motion is detected the user will receive a clip of the whole event moments after it has happened.

The Smart Pet Flap is packed full of features too. From letting you decide when your pet can or can't go outside from your mobile, to automatically opening if a fire is detected (along with a whole host of other features) - this really is the most advanced pet flap in the world.

REQUIREMENTS
We need 4 mock-up screens creating to show the UI of our app.
1. Camera Home Page
2. Camera Notifications Page
3. Pet Flap Fire Alarm Warning Page
4. Extreme Weather Warning Page

Optional - Happy to Pay the Winner Extra for these Designs
5. Start Up/Log In Page
6. Pet Flap Notification Example
7. Pet Flap Scheduler Page (your choice)
(SEE MARLOW APP DESIGN COMPETITION - ATTACHED)

STYLE GUIDE
As you'll see from our wireframes we want our app to be very minimal and modern. The predominant colour will be white but where colour is used it should be bright (see our colour palette - which we will provide shortly).

INSPIRATION
We love the UI of Tumbleweed (home surveillance). Also check out Pike (smart thermostat).
(SEE MARLOW UI EXAMPLES ATTACHED)

LOGO
We love our logo. Feel free to use it in creative ways.

So far we're also using it as a kind of beacon to indicate if everything is ok.

LOGO COLOURS & APP COLOURS
As mentioned, we are thinking of using the green logo to indicate that everything is ok (and also for the pet app in general). We reserve red for when something has happened (normally bad) and needs attention, like a fire alarm going off.

The app will be predominantly black and white with the odd minimal flash of colour (probably primary colour)
We'll upload a colour scheme as soon as we have it.

CONTACT
Please message us for more details - we'll do our best to reply promptly.

FUTURE WORK
We will need extra screens made straight after the competition is over and there should be additional regular work after this.

Target Market(s)

Our app will be used by young professionals, to young parents to grandparents. The design must be contemporary but timeless and easy to use no matter how good you are with technology.

Industry/Entity Type

Pet

Font styles to use
Sans Serif

Colors
faee3f
33a6d7
ec1f27
acd036
32b7a4

Requirements
Must have
• Beautiful, minimal design. Make sure you spend time looking at the Tumbleweed and Pike apps before starting.

For the videos make sure you use sensible images - that you'd expect to see from a monitor (high resolution images if possible)
Nice to have
• Creative use of our logo.
Should not have
• Too much detail/clutter/colours. Ugly fonts.

```html
<!DOCTYPE html>
<html lang="en">
<head>
<meta charset="utf-8">
<title>Marlow – Nursery Camera Notifications</title>
<link href="https://fonts.googleapis.com/css2?family=Inter:wght@300;400;600;700&display=swap" rel="stylesheet">
<style>
  :root {
    --ink: #1b1b1b;
    --bar: #231f20;
    --white: #ffffff;
    --status-bg: #f2f2f2;
    --list-bg: #f5f6f7;
    --rule: #b9b9b9;
    --rule-dark: #3a3a3a;
    --calm: #1fa84a;
    --brand: #acd036;
  }
  * { box-sizing: border-box; margin: 0; padding: 0; }
  html, body { width: 911px; height: 1200px; overflow: hidden; }
  body {
    font-family: "Inter", "Helvetica Neue", Arial, sans-serif;
    color: var(--ink);
    background: var(--list-bg);
  }
  .app { width: 911px; height: 1200px; display: flex; flex-direction: column; }

  .status-bar {
    height: 52px; background: var(--status-bg);
    display: flex; align-items: center; justify-content: space-between;
    padding: 0 20px; font-size: 26px; font-weight: 400;
    position: relative;
  }
  .status-left, .status-right { display: flex; align-items: center; gap: 10px; }
  .signal { display: flex; gap: 4px; }
  .signal span { width: 12px; height: 12px; border-radius: 50%; background: var(--ink); }
  .signal span.off { background: none; border: 1.5px solid var(--ink); }
  .status-time {
    position: absolute; left: 50%; transform: translateX(-50%);
    font-weight: 600;
  }

  .nav-bar {
    height: 84px; background: var(--bar); color: var(--white);
    display: flex; align-items: center; padding: 0 26px;
    position: relative;
  }
  .menu-icon { width: 36px; height: 28px; display: flex; flex-direction: column; justify-content: space-between; }
  .menu-icon span { height: 4px; background: var(--white); }
  .nav-title { margin-left: 60px; font-size: 30px; font-weight: 700; }
  .segmented {
    margin-left: auto; display: flex; border: 2px solid var(--white);
    height: 46px; font-size: 22px; font-weight: 700; letter-spacing: 0.5px;
  }
  .segmented span { display: flex; align-items: center; justify-content: center; padding: 0 24px; }
  .segmented .active { background: var(--white); color: var(--bar); position: relative; }
  .segmented .active::after {
    content: ""; position: absolute; bottom: -20px; left: 50%; transform: translateX(-50%);
    border: 9px solid transparent; border-top-color: var(--white);
  }
  .brand { margin-left: 26px; display: flex; align-items: center; gap: 10px; font-size: 28px; font-weight: 700; }
  .brand-dot { width: 22px; height: 22px; border-radius: 50%; background: var(--brand); }

  .page-header {
    height: 364px; background: var(--white);
    display: flex; justify-content: center; padding-top: 84px;
  }
  .header-block { width: 520px; }
  .header-block .top-rule { height: 4px; background: var(--rule-dark); }
  .page-title {
    font-size: 52px; font-weight: 300; line-height: 1.3;
    padding: 20px 0 22px; letter-spacing: -0.5px;
  }
  .header-block .mid-rule { height: 2px; background: var(--rule); }
  .change-camera {
    font-size: 26px; font-weight: 700; letter-spacing: 0.5px;
    padding: 18px 0 16px;
  }
  .header-block .bottom-rule { height: 2px; background: var(--rule); }

  .notification-list { list-style: none; background: var(--list-bg); border-top: 2px solid #d7d7d7; }
  .notification {
    height: 140px; display: flex; align-items: center;
    border-bottom: 2px solid #d7d7d7; padding: 0 40px 0 50px;
  }
  .notification-icon { width: 90px; height: 90px; display: flex; align-items: center; justify-content: center; }
  .notification-text { flex: 1; margin-left: 50px; font-size: 28px; line-height: 1.3; }
  .notification-time { font-weight: 700; display: block; }
  .view-button { display: flex; flex-direction: column; align-items: center; gap: 8px; font-size: 20px; font-weight: 600; }
  .play-circle { width: 58px; height: 58px; border-radius: 50%; background: var(--bar); display: flex; align-items: center; justify-content: center; }
  .calm-dot { width: 58px; height: 58px; border-radius: 50%; background: var(--calm); }
</style>
</head>
<body>
<div class="app">
  <header class="status-bar">
    <div class="status-left">
      <div class="signal"><span></span><span></span><span></span><span class="off"></span><span class="off"></span></div>
      <span>KESTREL</span>
      <svg width="28" height="22" viewBox="0 0 28 22"><path d="M2 8a17 17 0 0 1 24 0M6 12a11 11 0 0 1 16 0M10 16a5 5 0 0 1 8 0" fill="none" stroke="#1b1b1b" stroke-width="2.6"/><circle cx="14" cy="19.5" r="2" fill="#1b1b1b"/></svg>
    </div>
    <span class="status-time">4:21 PM</span>
    <div class="status-right">
      <svg width="16" height="26" viewBox="0 0 16 26"><path d="M2 7l12 12-6 5V2l6 5L2 19" fill="none" stroke="#1b1b1b" stroke-width="2"/></svg>
      <span>100%</span>
      <svg width="50" height="24" viewBox="0 0 50 24"><rect x="1" y="2" width="43" height="20" rx="3" fill="none" stroke="#1b1b1b" stroke-width="2"/><rect x="4" y="5" width="37" height="14" fill="#1b1b1b"/><rect x="45" y="8" width="4" height="8" fill="#1b1b1b"/></svg>
    </div>
  </header>

  <nav class="nav-bar">
    <div class="menu-icon"><span></span><span></span><span></span></div>
    <span class="nav-title">Cameras</span>
    <div class="segmented"><span>NOW</span><span class="active">EARLIER</span></div>
    <div class="brand"><span class="brand-dot"></span>Marlow</div>
  </nav>

  <section class="page-header">
    <div class="header-block">
      <div class="top-rule"></div>
      <h1 class="page-title">Nursery Camera<br>Notifications</h1>
      <div class="mid-rule"></div>
      <div class="change-camera">CHANGE CAMERA</div>
      <div class="bottom-rule"></div>
    </div>
  </section>

  <ul class="notification-list">
    <li class="notification">
      <div class="notification-icon">
        <svg width="84" height="60" viewBox="0 0 84 60" fill="none" stroke="#1b1b1b" stroke-width="4"><circle cx="42" cy="30" r="7"/><path d="M30 16a18 18 0 0 0 0 28M54 16a18 18 0 0 1 0 28M20 6a32 32 0 0 0 0 48M64 6a32 32 0 0 1 0 48"/></svg>
      </div>
      <p class="notification-text"><span class="notification-time">7:15am</span>There’s a lot of movement and noise.</p>
      <div class="view-button"><span class="play-circle"><svg width="20" height="22" viewBox="0 0 20 22"><path d="M3 1l16 10L3 21z" fill="#fff"/></svg></span>VIEW</div>
    </li>
    <li class="notification">
      <div class="notification-icon"><span class="calm-dot"></span></div>
      <p class="notification-text"><span class="notification-time">6:07am</span>All is calm.</p>
      <div class="view-button"><span class="play-circle"><svg width="20" height="22" viewBox="0 0 20 22"><path d="M3 1l16 10L3 21z" fill="#fff"/></svg></span>VIEW</div>
    </li>
    <li class="notification">
      <div class="notification-icon">
        <svg width="40" height="66" viewBox="0 0 40 66"><rect x="11" y="2" width="18" height="34" rx="9" fill="#1b1b1b"/><path d="M4 28a16 16 0 0 0 32 0" fill="none" stroke="#1b1b1b" stroke-width="4"/><path d="M20 44v14M8 62h24" stroke="#1b1b1b" stroke-width="4"/></svg>
      </div>
      <p class="notification-text"><span class="notification-time">5:32am</span>There’s some loud noise.</p>
      <div class="view-button"><span class="play-circle"><svg width="20" height="22" viewBox="0 0 20 22"><path d="M3 1l16 10L3 21z" fill="#fff"/></svg></span>VIEW</div>
    </li>
    <li class="notification">
      <div class="notification-icon">
        <svg width="40" height="90" viewBox="0 0 40 90"><path d="M20 2v16M12 11l8 9 8-9" fill="none" stroke="#1b1b1b" stroke-width="4"/><rect x="13" y="30" width="14" height="40" rx="7" fill="none" stroke="#1b1b1b" stroke-width="4"/><circle cx="20" cy="76" r="11" fill="#1b1b1b"/><rect x="17" y="50" width="6" height="24" fill="#1b1b1b"/></svg>
      </div>
      <p class="notification-text"><span class="notification-time">4:49am</span>The room temperature has just dropped to 16 degrees.</p>
      <div class="view-button"><span class="play-circle"><svg width="20" height="22" viewBox="0 0 20 22"><path d="M3 1l16 10L3 21z" fill="#fff"/></svg></span>VIEW</div>
    </li>
    <li class="notification">
      <div class="notification-icon">
        <svg width="84" height="60" viewBox="0 0 84 60" fill="none" stroke="#1b1b1b" stroke-width="4"><circle cx="42" cy="30" r="7"/><path d="M30 16a18 18 0 0 0 0 28M54 16a18 18 0 0 1 0 28M20 6a32 32 0 0 0 0 48M64 6a32 32 0 0 1 0 48"/></svg>
      </div>
      <p class="notification-text"><span class="notification-time">4:11am</span>There is a lot of movement.</p>
      <div class="view-button"><span class="play-circle"><svg width="20" height="22" viewBox="0 0 20 22"><path d="M3 1l16 10L3 21z" fill="#fff"/></svg></span>VIEW</div>
    </li>
  </ul>
</div>
</body>
</html>
```